Consultancy Business Card Design

We need a business card design for a new company based in singapore called FortyOne. FortyOne a boutique consultancy firm offering broad-based business solutions, from conception to re-invention, for ventures from new start-ups to long-running traditional businesses.
Its 2 main divisions (Food & Beverage Operations and Construction & Project Management) have access to a wide range of networks, knowledge bases, and resources to service its clients across numerous diverse sectors. This includes, and is not limited to, construction, F&B, and retail.
We are a company that combines the ambition, boldness and energy of one in the 20s with the dedication, level-headedness and dependability of one entering its 30s. Bridging the experiences of the old with ideals of the young, we draw on the positives of both to create a unique synergy.
We hope to see designs that fits our company profile.
Boutique
FortyOne(Company Name)
Marcus Leow (Name)
Principle Consultant (Title)
F&B and Hospitality (Division)
(+65) 8364 5170 (Contact no.)
marcus@fortyone-example.com.sg (Email)

```html
<!DOCTYPE html>
<html lang="en">
<head>
<meta charset="utf-8">
<title>FortyOne — Business Card</title>
<link rel="stylesheet" href="https://fonts.googleapis.com/css2?family=Raleway:wght@300;400;800&display=swap">
<style>
  :root {
    --page: #e6e6e6;
    --card-light: #ffffff;
    --card-dark: #4b4b4b;
    --ink: #1a1a1a;
    --ink-soft: #6b6b6b;
    --logo-ink: #ffffff;
  }
  * { margin: 0; padding: 0; box-sizing: border-box; }
  html, body { width: 1200px; height: 849px; overflow: hidden; }
  body {
    background: var(--page);
    font-family: "Raleway", sans-serif;
    color: var(--ink);
    position: relative;
  }
  .card {
    position: absolute;
    top: 272px;
    width: 520px;
    height: 305px;
    box-shadow: 0 6px 18px rgba(0,0,0,0.12);
  }
  .card--front { left: 50px; background: var(--card-light); }
  .card--back { left: 630px; background: var(--card-dark); display: flex; align-items: center; justify-content: center; }

  .logo-block {
    position: absolute;
    left: 0; top: 0;
    width: 250px; height: 118px;
    background: var(--card-dark);
    display: flex; align-items: center; justify-content: center;
  }
  .wordmark {
    font-weight: 800;
    color: var(--logo-ink);
    letter-spacing: 0.5px;
  }
  .logo-block .wordmark { font-size: 38px; }
  .card--back .wordmark { font-size: 78px; }

  .identity {
    position: absolute;
    right: 28px; top: 34px;
    text-align: right;
  }
  .identity__name { font-weight: 400; font-size: 19px; }
  .identity__title { font-weight: 300; font-size: 12px; color: var(--ink-soft); margin-top: 5px; }

  .contact {
    position: absolute;
    left: 32px; bottom: 40px;
    font-weight: 300;
  }
  .contact__name { font-size: 20px; font-weight: 400; }
  .contact__title { font-size: 12px; color: var(--ink-soft); margin: 4px 0 16px; }
  .contact__line { font-size: 12px; line-height: 1.6; }
</style>
</head>
<body>
  <section class="card card--front" aria-label="Card front">
    <div class="logo-block"><span class="wordmark">FortyOne</span></div>
    <div class="identity">
      <p class="identity__name">Marcus Leow</p>
      <p class="identity__title">F&amp;B and Hospitality</p>
    </div>
    <div class="contact">
      <p class="contact__name">Marcus Leow</p>
      <p class="contact__title">Principle Consultant</p>
      <p class="contact__line">(+65) 8364 5170</p>
      <p class="contact__line">marcus@fortyone-example.com.sg</p>
    </div>
  </section>

  <section class="card card--back" aria-label="Card back">
    <span class="wordmark">FortyOne</span>
  </section>
</body>
</html>
```